Flyer for Roadhaven 41Ter - Fresh Food Vending Machine in Helchteren

Project Description:
Roadhaven 41Ter has placed a new fresh food vending machine in Helchteren at KP Sodas (Lindeweg 517). We want to create an eye-catching, modern flyer to inform local residents about this vending machine and invite them to visit. The flyer will be distributed door-to-door in Helchteren.
Target Audience:
Residents of Helchteren and surrounding areas.
People looking for quick, fresh meals such as daily specials, wraps, poke bowls, soups, and pasta dishes.
Key Message:
Main title: "Helchteren, we’re here!"
Location: "Our brand-new fresh food vending machine is now at KP Sodas, Lindeweg 517!"
Available products: "Daily specials, wraps, poke bowls, soups, pasta dishes, and more."
Promotion: "For a limited time: with every product, you’ll receive a scratch card, and you always win!"
Style Guidelines:
Clean, professional, and inviting design.
Follow the new branding style of Roadhaven 41Ter (refer to the most recent posts on our Pictagram and Friendbook pages). Or see attachment for the layout inspiration.
Pictagram: www.pictagram-example.com/roadhaven41ter
Friendbook: www.friendbook-example.com/Roadhaven41
Do not use the older branding visible in earlier posts.
Format:
Flyer size: A5 (148 x 210 mm).
Additional Information:
Include our logos and social media accounts on the flyer.
Add a clear call-to-action, such as: "Visit us today!"
Ensure the flyer is easy to read and that all information is clear at a glance.
We look forward to seeing your creative and inspiring designs!

```html
<!DOCTYPE html>
<html lang="en">
<head>
<meta charset="utf-8">
<title>Roadhaven 41Ter – Helchteren flyer</title>
<link rel="stylesheet" href="https://fonts.googleapis.com/css2?family=Anton&family=Oswald:wght@300;400;500;600&display=swap">
<style>
  :root {
    --navy: #16206b;
    --blue: #1a44b4;
    --blue-bright: #2a8ad8;
    --red: #d2161c;
    --red-deep: #a30f14;
    --white: #ffffff;
  }
  * { margin: 0; padding: 0; box-sizing: border-box; }
  html, body { width: 846px; height: 1200px; overflow: hidden; }
  body { font-family: "Oswald", sans-serif; color: var(--white); }
  .flyer { position: relative; width: 846px; height: 1200px; overflow: hidden; background: var(--navy); }
  .backdrop { position: absolute; inset: 0; }
  .watermark-name {
    position: absolute; left: 600px; top: 78px;
    font-family: "Anton", sans-serif; font-size: 170px; line-height: 1;
    color: rgba(255,255,255,0.07);
    transform-origin: left top; transform: translate(200px, 0) rotate(90deg);
    white-space: nowrap; letter-spacing: 2px;
  }
  .brand { position: absolute; left: 55px; top: 52px; display: flex; align-items: center; gap: 10px; }
  .brand-mark { width: 26px; height: 26px; background: var(--blue-bright); }
  .brand-name { font-family: "Anton", sans-serif; font-size: 44px; line-height: 1; color: var(--white); letter-spacing: 0.5px; }
  .brand-rule { position: absolute; left: 50px; top: 136px; width: 140px; height: 5px; background: var(--red); }
  .headline { position: absolute; left: 46px; top: 176px; font-family: "Anton", sans-serif; line-height: 1; font-weight: 400; }
  .headline .city { display: block; font-size: 100px; color: var(--white); letter-spacing: 7px; }
  .headline .greeting { display: block; font-size: 86px; color: var(--red); margin-top: 2px; letter-spacing: 1px; }
  .block { position: absolute; left: 49px; }
  .block h2 { font-family: "Oswald", sans-serif; font-weight: 600; font-size: 26px; line-height: 1.1; letter-spacing: 0.2px; }
  .block p { font-weight: 300; font-size: 17px; line-height: 1.5; }
  .block p strong { font-weight: 500; }
  .location { top: 392px; }
  .products { top: 490px; }
  .products p { font-size: 15.5px; line-height: 1.35; }
  .product-card {
    position: absolute; left: 49px; top: 561px; width: 209px; height: 214px;
    border: 2px solid var(--white); border-radius: 12px;
    background: linear-gradient(160deg, #1e63bd 0%, #2f95db 100%);
    box-shadow: 0 6px 14px rgba(0,0,0,0.3);
    padding: 22px 0 0 22px;
  }
  .product-list { list-style: none; }
  .product-list li { font-weight: 600; font-size: 18.5px; line-height: 28px; padding-left: 16px; position: relative; }
  .product-list li::before { content: ""; position: absolute; left: 0; top: 12px; width: 6px; height: 6px; border-radius: 50%; background: var(--red); }
  .product-card .more { font-weight: 300; font-size: 14.5px; margin-top: 6px; }
  .offer-badge {
    position: absolute; left: 184px; top: 833px; width: 72px; height: 60px;
    background: #1c7fd6; border: 2px solid var(--white); border-radius: 50% 50% 50% 50% / 55% 55% 45% 45%;
    display: flex; align-items: center; justify-content: center; text-align: center;
    font-weight: 600; font-size: 12px; line-height: 1.3;
  }
  .promotion { top: 868px; }
  .promotion p { font-size: 15.5px; line-height: 1.4; }
  .contact { top: 972px; }
  .contact .cta { font-weight: 600; font-size: 24px; line-height: 1.3; }
  .contact .cta-sub { font-weight: 300; font-size: 24px; line-height: 1.3; }
  .social { top: 1090px; }
  .social p { font-weight: 500; font-size: 17px; margin-top: 6px; }
  .follow { position: absolute; left: 628px; top: 1090px; }
  .follow h2 { font-weight: 600; font-size: 24px; }
  .follow-links { display: flex; gap: 10px; margin-top: 8px; }
  .follow-link { display: flex; flex-direction: column; align-items: center; gap: 2px; }
  .follow-dot { width: 36px; height: 36px; border-radius: 50%; background: #1c86d8; }
  .follow-label { font-weight: 300; font-size: 9px; }
  .machine-photo {
    position: absolute; left: 363px; top: 345px; width: 483px; height: 690px;
    background: linear-gradient(110deg, #3a3b3f 0%, #1d1e21 45%, #505257 80%, #b9bcc1 100%);
    clip-path: polygon(0px 202px, 130px 196px, 130px 10px, 440px 0px, 483px 30px, 483px 660px, 440px 686px, 130px 672px, 130px 600px, 0px 594px);
  }
</style>
</head>
<body>
<main class="flyer">
  <svg class="backdrop" width="846" height="1200" viewBox="0 0 846 1200" aria-hidden="true">
    <defs>
      <radialGradient id="sky" cx="0.3" cy="0.45" r="0.8">
        <stop offset="0" stop-color="#2356c8"/>
        <stop offset="1" stop-color="#141c62"/>
      </radialGradient>
      <linearGradient id="field" x1="0" y1="0" x2="0" y2="1">
        <stop offset="0" stop-color="#c8151b"/>
        <stop offset="1" stop-color="#9c0e12"/>
      </linearGradient>
    </defs>
    <rect width="846" height="1200" fill="url(#sky)"/>
    <g fill="#ffffff" opacity="0.05">
      <polygon points="250,520 0,120 0,220"/>
      <polygon points="250,520 120,0 220,0"/>
      <polygon points="250,520 420,0 520,0"/>
      <polygon points="250,520 846,80 846,200"/>
      <polygon points="250,520 846,420 846,520"/>
      <polygon points="250,520 0,480 0,580"/>
    </g>
    <path d="M0,690 C20,760 50,760 90,730 C220,780 480,900 846,1000 L846,1200 L0,1200 Z" fill="url(#field)"/>
  </svg>

  <div class="watermark-name" aria-hidden="true">ROADHAVEN</div>

  <div class="brand">
    <span class="brand-mark" aria-hidden="true"></span>
    <span class="brand-name">Roadhaven 41Ter</span>
  </div>
  <div class="brand-rule" aria-hidden="true"></div>

  <h1 class="headline">
    <span class="city">HELCHTEREN,</span>
    <span class="greeting">WE’RE HERE!</span>
  </h1>

  <section class="block location">
    <h2>LOCATION:</h2>
    <p>Our brand-new fresh food vending machine is now at<br><strong>KP Sodas, Lindeweg 517!</strong></p>
  </section>

  <section class="block products">
    <h2>AVAILABLE PRODUCTS:</h2>
    <p>Looking for a quick, healthy meal? We’ve got you covered with:</p>
  </section>

  <div class="product-card">
    <ul class="product-list">
      <li>DAILY SPECIALS</li>
      <li>WRAPS</li>
      <li>POKE BOWLS</li>
      <li>SOUPS</li>
      <li>PASTA DISHES</li>
    </ul>
    <p class="more">And much more to explore!</p>
  </div>

  <div class="machine-photo" role="img" aria-label="Two black fresh food vending machines stocked with snacks, sandwiches and bottled drinks"></div>

  <div class="offer-badge">EXCITING<br>OFFER!</div>

  <section class="block promotion">
    <h2>PROMOTION:</h2>
    <p>For a limited time, every purchase comes<br>with a scratch card, and guess what? You always win!</p>
  </section>

  <section class="block contact">
    <h2>CONTACT US:</h2>
    <p class="cta">Visit us today at KP Sodas, Lindeweg 517</p>
    <p class="cta-sub">Quick, fresh meals are just a few steps away!</p>
  </section>

  <section class="block social">
    <h2>SOCIAL MEDIA:</h2>
    <p>Stay updated on our latest offerings!</p>
  </section>

  <section class="follow">
    <h2>FOLLOW US ON:</h2>
    <div class="follow-links">
      <div class="follow-link"><span class="follow-dot" aria-hidden="true"></span><span class="follow-label">Pictagram</span></div>
      <div class="follow-link"><span class="follow-dot" aria-hidden="true"></span><span class="follow-label">Friendbook</span></div>
    </div>
  </section>
</main>
</body>
</html>
```